2 sided flyer for Insurance Servics

Would like a flyer that talks about who we are, our services, and our process. Attaching relevant information, as well as our Logo and other logos for a few larger insurance carriers that we have access to.

Target Market(s)

Financial Advisors and Insurance Agents

Industry/Entity Type

Finance and Insurance

Colors
0054AA
0677BA
7BADD7
CADEEF
E8F1F8
F0912C
F2A743
F7CA91
FBE8D2
FDF5EE

Requirements
Must have
• Lists, bullet points, pictures, and logos uploaded

```html
<!DOCTYPE html>
<html lang="en">
<head>
<meta charset="utf-8">
<title>Harborline Insurance Network – Two-Sided Flyer</title>
<link href="https://fonts.googleapis.com/css2?family=Montserrat:wght@500;700;800;900&family=Open+Sans:wght@400;600;700&display=swap" rel="stylesheet">
<style>
:root{
  --navy:#27266d;
  --navy-deep:#1d1c57;
  --blue:#0054aa;
  --blue-mid:#0677ba;
  --blue-soft:#7badd7;
  --blue-pale:#cadeef;
  --blue-mist:#e8f1f8;
  --orange:#f0912c;
  --orange-warm:#f2a743;
  --orange-soft:#f7ca91;
  --orange-pale:#fbe8d2;
  --cream:#fdf5ee;
  --ink:#2b2b3a;
  --muted:#5b6072;
  --white:#ffffff;
}
*{box-sizing:border-box;margin:0;padding:0}
html,body{width:1200px;height:2400px;overflow:hidden;background:#ffffff}
body{position:relative;font-family:"Open Sans",Arial,sans-serif;color:var(--ink)}
.page{position:absolute;width:880px;height:1140px;background:var(--white);box-shadow:0 6px 24px rgba(20,20,60,.18);overflow:hidden}
.page--front{left:210px;top:30px}
.page--back{left:110px;top:1230px}

/* front header */
.hero{position:absolute;left:0;top:0;width:880px;height:420px;background:var(--navy)}
.hero__photo{position:absolute;right:0;top:0;width:470px;height:420px;background:linear-gradient(135deg,#d9d2c6,#b9a994 55%,#8c7a66);clip-path:polygon(18% 0,100% 0,100% 100%,0 100%)}
.brand{position:absolute;left:40px;top:36px;display:flex;align-items:center;gap:10px}
.brand__mark{width:46px;height:46px;background:var(--white)}
.brand__name{font-family:"Montserrat",Arial,sans-serif;font-weight:800;font-size:15px;line-height:1.15;color:var(--white);text-transform:uppercase;letter-spacing:.5px}
.hero__title{position:absolute;left:40px;top:150px;font-family:"Montserrat",Arial,sans-serif;font-weight:900;text-transform:uppercase;color:var(--white);line-height:1.02}
.hero__title .l1{font-size:30px;display:block}
.hero__title .l2{font-size:50px;display:block;color:var(--orange)}
.hero__title .l3{font-size:44px;display:block}
.hero__stripe{position:absolute;left:40px;top:345px;width:90px;height:6px;background:var(--orange)}

/* front body */
.col{position:absolute}
.col--about{left:40px;top:450px;width:380px}
.col--why{left:450px;top:440px;width:400px;height:600px;background:var(--blue-mist);padding:26px 26px}
.h2{font-family:"Montserrat",Arial,sans-serif;font-weight:800;color:var(--navy);font-size:26px;margin-bottom:10px}
.h2 .accent{color:var(--orange)}
.body{font-size:12.5px;line-height:1.55;color:var(--muted)}
.carriers-title{margin-top:26px;font-family:"Montserrat",Arial,sans-serif;font-weight:800;font-size:20px;color:var(--navy)}
.carriers{margin-top:14px;display:grid;grid-template-columns:1fr 1fr;gap:16px 22px}
.carrier{height:52px;border-radius:4px;background:var(--blue-pale)}
.carrier:nth-child(3n){background:var(--orange-pale)}
.why__lead{font-weight:700;font-size:13px;color:var(--navy);line-height:1.45;margin-bottom:16px}
.reason{display:flex;gap:14px;margin-bottom:16px}
.reason__icon{flex:0 0 44px;height:44px;border-radius:50%;background:var(--orange);display:flex;align-items:center;justify-content:center}
.reason__title{font-family:"Montserrat",Arial,sans-serif;font-weight:800;font-size:12.5px;color:var(--navy);text-transform:uppercase;line-height:1.2;margin-bottom:3px}
.reason__text{font-size:11px;line-height:1.45;color:var(--muted)}
.why__note{font-size:11px;line-height:1.5;color:var(--muted);margin-top:4px}
.why__web{font-weight:700;font-size:12px;color:var(--blue);margin-top:8px}

/* footer */
.footer{position:absolute;left:0;bottom:0;width:880px;height:80px;background:var(--navy);display:flex;align-items:center;padding:0 40px;gap:34px}
.footer__label{font-family:"Montserrat",Arial,sans-serif;font-weight:900;font-size:28px;color:var(--orange);text-transform:uppercase}
.footer__item{display:flex;align-items:center;gap:8px;color:var(--white);font-size:14px;font-weight:600}
.footer__dot{width:24px;height:24px;border-radius:50%;background:var(--orange);display:flex;align-items:center;justify-content:center}

/* back */
.back-left{position:absolute;left:40px;top:40px;width:390px}
.back-right{position:absolute;left:455px;top:30px;width:395px}
.value-sub{font-family:"Montserrat",Arial,sans-serif;font-weight:800;font-size:15px;color:var(--blue);margin:4px 0 6px}
.bullet-list{list-style:none}
.bullet-list li{position:relative;padding-left:16px;font-size:11.5px;line-height:1.5;color:var(--muted);margin-bottom:6px}
.bullet-list li::before{content:"";position:absolute;left:2px;top:6px;width:7px;height:7px;border-radius:50%;background:var(--orange)}
.bullet-list strong{color:var(--navy)}
.callout{background:var(--blue-mist);border-left:5px solid var(--blue);padding:12px 14px;font-size:11.5px;line-height:1.5;color:var(--navy);font-weight:600;margin:12px 0}
.callout--warm{background:var(--orange-pale);border-left-color:var(--orange)}
.process{margin-top:14px;background:var(--navy);padding:18px 22px;color:var(--white)}
.process__title{font-family:"Montserrat",Arial,sans-serif;font-weight:900;font-size:24px;color:var(--white);margin-bottom:10px;text-align:center}
.step{margin-bottom:10px}
.step__head{display:flex;align-items:center;gap:8px;font-family:"Montserrat",Arial,sans-serif;font-weight:800;font-size:13.5px;color:var(--orange-warm);margin-bottom:3px}
.step__num{width:20px;height:20px;border-radius:50%;background:var(--orange);color:var(--white);font-size:11px;display:flex;align-items:center;justify-content:center}
.step ul{list-style:none}
.step li{font-size:10.5px;line-height:1.45;color:var(--blue-pale);padding-left:28px;position:relative}
.step li::before{content:"›";position:absolute;left:16px;color:var(--orange-soft)}
.concierge{margin-top:14px}
.map{height:250px;background:linear-gradient(160deg,var(--blue-mist),var(--blue-pale))}
.right-list{list-style:none;margin-top:8px}
.right-list li{font-size:11px;line-height:1.45;color:var(--muted);padding:4px 0 4px 18px;position:relative;border-bottom:1px solid var(--blue-mist)}
.right-list li::before{content:"";position:absolute;left:2px;top:9px;width:8px;height:8px;background:var(--blue)}
.right-list strong{color:var(--navy)}
</style>
</head>
<body>

<section class="page page--front">
  <header class="hero">
    <div class="hero__photo" role="img" aria-label="Photo of two advisors reviewing documents at a laptop"></div>
    <div class="brand">
      <div class="brand__mark"></div>
      <div class="brand__name">Harborline<br>Insurance<br>Network</div>
    </div>
    <h1 class="hero__title">
      <span class="l1">Full-Service Life Insurance</span>
      <span class="l2">Brokerage</span>
      <span class="l3">General Agency</span>
    </h1>
    <div class="hero__stripe"></div>
  </header>

  <div class="col col--about">
    <h2 class="h2">About Us</h2>
    <p class="body">Harborline Insurance Network is a full-service life insurance Brokerage General Agency (BGA) serving financial advisors, independent insurance agents and banks throughout the United States. Having served our customers for over 25 years, we are committed to helping financial advisors enhance their value to clients while building stronger practices through better insurance solutions.</p>
    <h3 class="carriers-title">List of Carriers Include</h3>
    <div class="carriers">
      <div class="carrier"></div><div class="carrier"></div>
      <div class="carrier"></div><div class="carrier"></div>
      <div class="carrier"></div><div class="carrier"></div>
      <div class="carrier"></div><div class="carrier"></div>
    </div>
  </div>

  <aside class="col col--why">
    <h2 class="h2">Why <span class="accent">HIN?</span></h2>
    <p class="why__lead">When you choose to work with HIN, you will add value to your firm…overnight!</p>

    <div class="reason">
      <div class="reason__icon"><svg width="22" height="22" viewBox="0 0 24 24" fill="none" stroke="#fff" stroke-width="2.4"><path d="M5 12l4 4 10-10"/></svg></div>
      <div><div class="reason__title">Ambassador &amp; Relationship Partner</div><p class="reason__text">We become an extension of your team, with a dedicated partner who knows your clients, your firm and your goals.</p></div>
    </div>
    <div class="reason">
      <div class="reason__icon"><svg width="22" height="22" viewBox="0 0 24 24" fill="none" stroke="#fff" stroke-width="2.4"><path d="M5 12l4 4 10-10"/></svg></div>
      <div><div class="reason__title">Experienced Insurance Specialists</div><p class="reason__text">Our team of case designers and underwriters has decades of experience placing complex cases with top-rated carriers.</p></div>
    </div>
    <div class="reason">
      <div class="reason__icon"><svg width="22" height="22" viewBox="0 0 24 24" fill="none" stroke="#fff" stroke-width="2.4"><path d="M5 12l4 4 10-10"/></svg></div>
      <div><div class="reason__title">Customized Premium Service</div><p class="reason__text">Every case receives personal attention, from the first illustration through policy delivery and beyond.</p></div>
    </div>
    <div class="reason">
      <div class="reason__icon"><svg width="22" height="22" viewBox="0 0 24 24" fill="none" stroke="#fff" stroke-width="2.4"><path d="M5 12l4 4 10-10"/></svg></div>
      <div><div class="reason__title">Save Time and Money</div><p class="reason__text">We handle the paperwork, follow-up and carrier communication so you can stay focused on your clients.</p></div>
    </div>
    <p class="why__note">We are compensated by the carriers, so there is no added cost to you or your clients. Visit our website to learn more about how we can support your practice.</p>
    <p class="why__web">www.harborline-network.com</p>
  </aside>

  <footer class="footer">
    <span class="footer__label">Contact Us</span>
    <span class="footer__item"><span class="footer__dot"><svg width="12" height="12" viewBox="0 0 24 24" fill="none" stroke="#fff" stroke-width="2.6"><rect x="3" y="6" width="18" height="12"/><path d="M3 6l9 7 9-7"/></svg></span>contact@harborline-network.com</span>
    <span class="footer__item"><span class="footer__dot"><svg width="12" height="12" viewBox="0 0 24 24" fill="none" stroke="#fff" stroke-width="2.6"><circle cx="12" cy="12" r="9"/><path d="M3 12h18M12 3c3 3 3 15 0 18M12 3c-3 3-3 15 0 18"/></svg></span>www.harborline-network.com</span>
  </footer>
</section>

<section class="page page--back">
  <div class="back-left">
    <h2 class="h2">Our <span class="accent">Value</span></h2>
    <h3 class="value-sub">Our Point of Sale Strategies</h3>
    <p class="body">We work directly with agents and advisors to provide experienced assistance for immediate client needs, as well as long-term planning strategies.</p>
    <ul class="bullet-list" style="margin-top:8px">
      <li><strong>Case Design:</strong> tailored illustrations and carrier comparisons for every client scenario.</li>
      <li><strong>Advanced Markets:</strong> estate, business and legacy planning support from our specialists.</li>
      <li><strong>Field Underwriting:</strong> quick, informal reviews to find the best offer before applying.</li>
    </ul>
    <div class="callout">Third-party review and pre-approval of cases gives you confidence before the client ever signs an application.</div>

    <div class="process">
      <h3 class="process__title">Our Process</h3>
      <div class="step">
        <div class="step__head"><span class="step__num">1</span>Intake &amp; Analysis</div>
        <ul><li>Review client goals, health history and existing coverage</li><li>Prepare carrier quotes and informal underwriting</li></ul>
      </div>
      <div class="step">
        <div class="step__head"><span class="step__num">2</span>Licensing &amp; Appointment</div>
        <ul><li>Fast contracting with the carriers you need</li><li>Ongoing support for state licensing requirements</li></ul>
      </div>
      <div class="step">
        <div class="step__head"><span class="step__num">3</span>Applications &amp; Underwriting</div>
        <ul><li>Application review, exams and medical records ordered</li><li>Daily status updates until a final offer is made</li></ul>
      </div>
      <div class="step">
        <div class="step__head"><span class="step__num">4</span>Policy Delivery &amp; Payout</div>
        <ul><li>Delivery requirements collected and policy placed</li><li>Commissions processed promptly and accurately</li></ul>
      </div>
    </div>

    <div class="concierge">
      <h3 class="value-sub">Our Concierge Service Team</h3>
      <p class="body">A dedicated case manager follows every file from submission to placement, keeping you informed at each step.</p>
    </div>
  </div>

  <div class="back-right">
    <div class="map" role="img" aria-label="Map of the United States showing the states where the agency serves advisors"></div>
    <div class="callout callout--warm">"We are the bridge for advisors, guiding the agent's team and clients through every step of the case."</div>
    <ul class="right-list">
      <li><strong>Informal Quotes</strong> – fast, no-obligation pricing across multiple carriers.</li>
      <li><strong>Policy Reviews</strong> – in-force analysis to find better value for existing coverage.</li>
      <li><strong>Term Conversions</strong> – identify conversion options before deadlines pass.</li>
      <li><strong>Long-Term Care</strong> – hybrid and traditional solutions for lasting protection.</li>
      <li><strong>Annuities</strong> – income and accumulation products from leading carriers.</li>
      <li><strong>Disability Income</strong> – individual and business coverage for your clients.</li>
    </ul>
    <div class="callout">"Advisors can be as involved as they like; we handle the details so the sale stays on track."</div>
    <ul class="right-list">
      <li><strong>Marketing Support</strong> – ready-to-use materials and client seminars.</li>
      <li><strong>Training</strong> – product and sales education for your team.</li>
      <li><strong>Case Tracking</strong> – online access to case status at any time.</li>
      <li><strong>Dedicated Staff</strong> – one point of contact for every case.</li>
    </ul>
    <div class="callout callout--warm">"Your clients receive the attention and service that reflects well on your firm."</div>
  </div>

  <footer class="footer">
    <span class="footer__label">Contact Us</span>
    <span class="footer__item"><span class="footer__dot"><svg width="12" height="12" viewBox="0 0 24 24" fill="none" stroke="#fff" stroke-width="2.6"><rect x="3" y="6" width="18" height="12"/><path d="M3 6l9 7 9-7"/></svg></span>contact@harborline-network.com</span>
    <span class="footer__item"><span class="footer__dot"><svg width="12" height="12" viewBox="0 0 24 24" fill="none" stroke="#fff" stroke-width="2.6"><circle cx="12" cy="12" r="9"/><path d="M3 12h18M12 3c3 3 3 15 0 18M12 3c-3 3-3 15 0 18"/></svg></span>www.harborline-network.com</span>
  </footer>
</section>

</body>
</html>
```